Poster Design for Photography Exhibit

We are looking for a poster design for a photography exhibit featuring high-end fashion and celebrity photography.

Name of the exhibit is "TOBIAS WRENLEY: AFTERGLOW" (please use Helvetica Black all cap for show name.

Poster is LANDSCAPE format (2 units wide by 1 unit high).

Unfortunately due to legal reasons, we cannot use any actual Tobias Wrenley photos. No can we use fashions or people on the poster!

We are looking for a high-end, sexy, bold provocative design that captures the excitement and glamour of a fashion photo shoot.

Target Market(s)

Men and Women interested in Fashion Photography and art photography in general

Industry/Entity Type

Fashion

Requirements
Must have
• landscape format, name of exhibit in Helvetica Black all caps
Nice to have
• Can be grayscale or color.
Should not have
• Logos or brand names

```html
<!DOCTYPE html>
<html lang="en">
<head>
<meta charset="utf-8">
<title>Tobias Wrenley: Afterglow — Exhibition Poster</title>
<link rel="stylesheet" href="https://fonts.googleapis.com/css2?family=Inter:wght@400;500;900&display=swap">
<style>
  :root {
    --paper: #ffffff;
    --ink: #000000;
    --text: #1a1a1a;
    --photo-dark: #141414;
    --photo-mid: #7a7a7a;
    --photo-light: #d9d9d9;
  }
  * { margin: 0; padding: 0; box-sizing: border-box; }
  html, body {
    width: 1200px;
    height: 600px;
    overflow: hidden;
    background: var(--paper);
  }
  .poster {
    position: relative;
    width: 1200px;
    height: 600px;
    overflow: hidden;
    background: var(--paper);
    font-family: "Inter", Helvetica, Arial, sans-serif;
    color: var(--text);
  }
  .website {
    position: absolute;
    left: 62px;
    top: 44px;
    font-size: 13px;
    font-weight: 500;
    color: var(--ink);
  }
  .hero-photo {
    position: absolute;
    left: 0;
    top: 80px;
    width: 560px;
    height: 520px;
    background:
      radial-gradient(ellipse 150px 140px at 270px 200px, var(--photo-light) 0%, var(--photo-mid) 55%, rgba(40,40,40,0) 100%),
      radial-gradient(ellipse 330px 330px at 210px 330px, var(--photo-dark) 0%, rgba(30,30,30,0.85) 45%, rgba(255,255,255,0) 100%);
  }
  .title-band {
    position: absolute;
    left: 440px;
    width: 760px;
    background: var(--ink);
    color: var(--paper);
    font-weight: 900;
    text-transform: uppercase;
    white-space: nowrap;
    overflow: hidden;
  }
  .title-text {
    display: inline-block;
    transform-origin: left center;
  }
  .title-artist {
    top: 152px;
    height: 54px;
    font-size: 66px;
    line-height: 52px;
    letter-spacing: -2.5px;
    padding-left: 4px;
  }
  .title-artist .title-text {
    transform: scaleX(0.98);
  }
  .title-show {
    top: 220px;
    height: 132px;
    font-size: 126px;
    line-height: 162px;
    letter-spacing: -4px;
    padding-left: 4px;
  }
  .title-show .title-text {
    transform: scaleX(0.86);
  }
  .intro {
    position: absolute;
    right: 75px;
    top: 360px;
    width: 700px;
    text-align: right;
    font-size: 13.5px;
    line-height: 19.5px;
    color: var(--text);
  }
  .dates {
    position: absolute;
    right: 75px;
    top: 474px;
    text-align: right;
    font-size: 24px;
    color: var(--text);
  }
  .venue-note {
    position: absolute;
    right: 75px;
    top: 510px;
    text-align: right;
    font-size: 13px;
    color: var(--text);
  }
</style>
</head>
<body>
  <main class="poster">
    <div class="website">www.yourwebsite.com</div>

    <div class="hero-photo" role="img" aria-label="Black and white close-up photograph of a vintage camera lens, fading into white"></div>

    <h1>
      <span class="title-band title-artist"><span class="title-text">Tobias Wrenley :</span></span>
      <span class="title-band title-show"><span class="title-text">Afterglow</span></span>
    </h1>

    <p class="intro">
      Lorem ipsum dolor sit amet, consectetur adipiscing elit. Curabitur si<br>
      t amet lacus quis lectus suscipit mollis. Morbi varius ullamcorper fermentum. Nulla in nisi<br>
      eu enim vulputate hendrerit. Nullam faucibus egestas molestie. Ut a libero at odio
    </p>

    <p class="dates">7-27 June 2013, Location St.</p>
    <p class="venue-note">aucibus egestas molestie. Ut a libero at odio</p>
  </main>
</body>
</html>
```